Corroway Medical Imaging marketing poster

A poster to advertise our services. Something outstanding that catches the eye. Will be displayed at medical centres. Needs to advertise the following:
Opening hours - Mon-fri 8am-5:30pm Sat 8am-12:30
Services offered: Ultrasound, CT, Xray, Conebeam CT, Barium Studies, Injections and Biopsies, 3D/4D pregnancy scans.
We Bulk Bill concession card holders and under 18's
Locally owned and operated
www.corrowaymedicalimaging.example.au
include contact details also Tel: 96384027 Fax: 9638 4093

```html
<!DOCTYPE html>
<html lang="en">
<head>
<meta charset="utf-8">
<title>Corroway Medical Imaging — Poster</title>
<link rel="stylesheet" href="https://fonts.googleapis.com/css2?family=Open+Sans:wght@400;600&family=Roboto:wght@500;700;900&display=swap">
<style>
  :root {
    --stage: #151515;
    --paper: #ffffff;
    --brand-blue: #00adee;
    --brand-green: #a8cb3a;
    --accent-red: #e8452c;
    --label-lime: #d5e27c;
    --ink: #111111;
    --ink-soft: #2b2b2b;
    --photo-light: #e9e9e9;
    --photo-mid: #cfcfcf;
  }
  * { box-sizing: border-box; margin: 0; padding: 0; }
  html, body { width: 1200px; height: 1200px; overflow: hidden; background: var(--stage); }
  .poster {
    position: absolute; left: 166px; top: 38px;
    width: 868px; height: 1124px;
    background: var(--paper); overflow: hidden;
    font-family: "Roboto", Arial, sans-serif;
  }

  .brand {
    position: absolute; left: 140px; top: 62px;
    display: flex; align-items: center; gap: 12px;
    font-family: "Open Sans", Arial, sans-serif; font-weight: 400;
    font-size: 26px; color: var(--ink-soft);
  }
  .brand__dot { width: 22px; height: 22px; border-radius: 50%; background: var(--brand-blue); }

  .hero-photo {
    position: absolute; left: 0; top: 166px; width: 868px; height: 334px;
    background: linear-gradient(90deg, var(--photo-mid) 0%, var(--photo-light) 45%, #f4f4f4 70%, #dcdcdc 100%);
  }
  .hero-title {
    position: absolute; left: 0; top: 256px; width: 478px; height: 154px;
    background: var(--paper);
    border-top: 3px solid #d9d9d9; border-bottom: 3px solid #d9d9d9;
    box-shadow: 0 3px 6px rgba(0,0,0,.15);
    font-family: "Open Sans", Arial, sans-serif; font-weight: 400;
    text-align: right; padding-right: 28px;
  }
  .hero-title__name { display: block; font-size: 74px; line-height: 1; color: var(--ink-soft); margin-top: 16px; letter-spacing: -2px; }
  .hero-title__sub { display: block; font-size: 44px; line-height: 1.1; color: var(--brand-blue); letter-spacing: -1px; }

  .pill {
    position: absolute; background: var(--accent-red); color: #fff;
    font-weight: 500; border-radius: 14px; text-align: center;
  }
  .pill--hours { left: 320px; top: 532px; width: 227px; height: 45px; line-height: 45px; font-size: 21px; letter-spacing: .5px; }
  .pill--contact { left: 514px; top: 1022px; width: 92px; height: 29px; line-height: 29px; font-size: 15px; border-radius: 15px; }

  .portrait {
    position: absolute; top: 577px; width: 168px; height: 166px;
    border: 2px solid var(--brand-blue); border-radius: 12px;
    background: linear-gradient(180deg, #ffffff 0%, #eef3f7 100%);
  }
  .portrait--left { left: 42px; }
  .portrait--right { left: 658px; }

  .hours { position: absolute; left: 250px; width: 380px; text-align: center; font-weight: 900; }
  .hours__day { color: var(--brand-blue); font-size: 36px; letter-spacing: 1px; line-height: 1; }
  .hours__time { color: var(--ink); font-size: 36px; letter-spacing: 1px; line-height: 1; margin-top: 4px; }
  .hours--week { top: 588px; }
  .hours--sat { top: 684px; }
  .hours__rule {
    position: absolute; left: 275px; top: 671px; width: 318px; height: 3px;
    background: linear-gradient(90deg, transparent, var(--brand-green) 30%, var(--brand-green) 70%, transparent);
  }

  .services {
    position: absolute; left: 0; top: 794px; width: 868px; height: 204px;
    background: var(--brand-blue); text-align: center; color: #fff;
  }
  .services__label {
    display: inline-block; background: var(--label-lime); color: var(--ink);
    font-weight: 700; font-size: 30px; letter-spacing: 1.5px;
    height: 36px; line-height: 38px; padding: 0 10px;
  }
  .services__list { margin-top: 6px; font-weight: 700; font-size: 30px; line-height: 37px; }

  .contact { position: absolute; right: 57px; top: 1009px; text-align: right; font-weight: 700; color: var(--ink); }
  .contact__line { font-size: 22px; letter-spacing: 1.5px; line-height: 28px; white-space: pre; }
  .contact__web { position: absolute; right: 57px; top: 1070px; font-family: "Open Sans", Arial, sans-serif; font-size: 15px; letter-spacing: 2.4px; color: var(--ink); }
</style>
</head>
<body>
<main class="poster">
  <div class="brand"><span class="brand__dot"></span><span>Corroway Medical Imaging</span></div>

  <div class="hero-photo" role="img" aria-label="Photograph of a doctor's white coat with a stethoscope and pens in the pocket"></div>
  <h1 class="hero-title">
    <span class="hero-title__name">CORROWAY</span>
    <span class="hero-title__sub">MEDICAL IMAGING</span>
  </h1>

  <div class="pill pill--hours">OPENING HOURS</div>
  <div class="portrait portrait--left" role="img" aria-label="Illustration of a male doctor with a stethoscope"></div>
  <div class="portrait portrait--right" role="img" aria-label="Illustration of a female doctor with a stethoscope"></div>

  <div class="hours hours--week">
    <div class="hours__day">MONDAY - FRIDAY</div>
    <div class="hours__time">8AM - 5:30PM</div>
  </div>
  <div class="hours__rule"></div>
  <div class="hours hours--sat">
    <div class="hours__day">SATURDAY</div>
    <div class="hours__time">8AM - 12:30PM</div>
  </div>

  <section class="services">
    <h2 class="services__label">SERVICES OFFERED</h2>
    <p class="services__list">
      Ultrasound, CT, Xray, Conebeam CT, Barium Studies,<br>
      Injections and Biopsies, 3D/4D pregnancy scans.<br>
      We Bulk Bill concession card holders and under 18's<br>
      Locally owned and operated
    </p>
  </section>

  <div class="pill pill--contact">CONTACT</div>
  <div class="contact">
    <div class="contact__line">Tel  :  96384027</div>
    <div class="contact__line">Fax  : 9638 4093</div>
  </div>
  <div class="contact__web">www.corrowaymedicalimaging.example.au</div>
</main>
</body>
</html>
```